Letter Head Design - Finance industry

Design a letterhead to match the logo. Needs to be clean, simple and crisp. I'm open to suggestions. Will be using the logo that was submitted last with the W crossed over

Target Market(s)

Small medium businesses and government department's

Industry/Entity Type

Industry

Font styles to use
Sans Serif

Colors
cadf82
bcd85c
acd036
9bcb3c
e9e9e9
aaaaaa
000000
7f7f7f
b7b7b7

Requirements
Must have
• Need to display: Logo, Business address, ABN number, ASIC register number, contact phone, website, company email. Details are as per below:

Suite 4B Level 17
Marlowe Crest House
9 Tindall Lane
Sydney NSW 2000
Landline Ph: 02 5193 4620
Ph: 1300 4719 55
Email: enquiries@coinharbourco.com.au
W: www.coinharbourco.com.au

On the footer, the details below need to be specified:
ABN: 47 381 950 623
ASIC Registration Number: 31 749218605

Should not have
• No imagery or design that is not in line with the logo

```html
<!DOCTYPE html>
<html lang="en">
<head>
<meta charset="utf-8">
<title>Coin Harbour Co — Letterhead</title>
<link rel="stylesheet" href="https://fonts.googleapis.com/css2?family=Open+Sans:ital,wght@0,300;0,400;0,600;1,300&display=swap">
<style>
  :root {
    --leaf-green: #9bcb3c;
    --leaf-light: #acd036;
    --ink: #000000;
    --ink-soft: #7f7f7f;
    --ink-muted: #aaaaaa;
    --paper: #ffffff;
    --backdrop: #e9e9e9;
    --signature-tone: #d6d6d6;
  }
  * { box-sizing: border-box; margin: 0; padding: 0; }
  html, body {
    width: 1200px; height: 1000px; overflow: hidden;
    background: var(--backdrop);
    font-family: "Open Sans", Arial, sans-serif;
  }
  .letterhead {
    position: absolute; left: 282px; top: 50px;
    width: 636px; height: 900px;
    background: var(--paper);
    box-shadow: 0 2px 10px rgba(0,0,0,0.12);
  }
  .brand {
    position: absolute; display: flex; align-items: center; gap: 8px;
  }
  .brand-dot {
    border-radius: 50%; background: var(--leaf-green); flex: none;
  }
  .brand-name {
    font-weight: 600; color: var(--ink); white-space: nowrap; line-height: 1;
  }
  .brand--header { left: 56px; top: 52px; }
  .brand--header .brand-dot { width: 30px; height: 30px; }
  .brand--header .brand-name { font-size: 20px; }
  .brand--footer { right: 56px; top: 708px; }
  .brand--footer .brand-dot { width: 18px; height: 18px; }
  .brand--footer .brand-name { font-size: 12px; }

  .letter-body {
    position: absolute; left: 56px; top: 190px; width: 524px;
    color: var(--ink-soft); font-weight: 300; font-size: 9.5px; line-height: 15px;
  }
  .salutation {
    font-style: italic; font-size: 12px; color: #444; margin-bottom: 18px;
  }
  .letter-body p { margin-bottom: 20px; text-align: justify; }
  .sign-off {
    position: absolute; right: 56px; top: 540px;
    font-style: italic; font-weight: 300; font-size: 11px; color: #444;
  }
  .signature {
    position: absolute; left: 380px; top: 640px; width: 120px; height: 36px;
    background: linear-gradient(90deg, transparent, var(--signature-tone), transparent);
    border-radius: 18px;
  }
  .footer-rule {
    position: absolute; left: 56px; right: 56px; top: 736px;
    height: 1px; background: var(--leaf-light);
  }
  .contact-details {
    position: absolute; left: 56px; right: 56px; top: 746px;
    text-align: center; color: var(--ink-soft);
    font-size: 6.4px; line-height: 10px; font-weight: 400;
  }
</style>
</head>
<body>
  <main class="letterhead">
    <header class="brand brand--header">
      <span class="brand-dot"></span>
      <span class="brand-name">Coin Harbour Co</span>
    </header>

    <section class="letter-body">
      <p class="salutation">Dear Client,</p>
      <p>Lorem ipsum dolor sit amet, consectetur adipiscing elit. Nulla sodales nisi vitae lorem ipsum dolor sit amet, consectetur adipiscing elit. Suspendisse feugiat erat nisl, a facilisis risus eleifend sed. Aliquam mauris enim, fermentum eu lacinia sit amet, laoreet eu leo. Nullam eleifend nulla in libero tristique, ac vulputate odio tincidunt. Etiam non condimentum tortor. Integer suscipit neque nec odio porttitor cursus. Phasellus a sapien blandit, suscipit justo id, condimentum ante. Morbi tristique justo risus, id mattis dui molestie ut. Nullam volutpat ut quam commodo faucibus. Pellentesque urna est, interdum in elit quis, pharetra elementum orci. Nam pharetra velit molestie justo placerat scelerisque.</p>
      <p>Sed est tellus, rutrum in nisl a, consequat sollicitudin elit. Aliquam vitae vestibulum felis. Morbi iaculis nunc volutpat diam ullamcorper vestibulum. Nulla facilisi. Aenean accumsan gravida orci, vitae consectetur justo aliquet et. Curabitur vehicula tempus dolor, a gravida metus vestibulum sit amet. Integer non erat elementum, malesuada metus vel, fermentum lectus. Etiam sit amet nisl ac augue semper ultrices.</p>
      <p>Nulla tincidunt molestie libero vel pretium. Donec condimentum nulla sit amet risus semper imperdiet. Duis congue eros nec diam blandit, et pellentesque sapien auctor. Curabitur iaculis enim lectus, in imperdiet mauris mattis eget. Etiam ac ornare metus. Mauris risus leo, egestas at dolor a, ultrices adipiscing est. Nunc faucibus scelerisque mollis. Pellentesque aliquet mauris tellus, id dignissim risus viverra et. Mauris venenatis lobortis eros. Nam id diam in ligula malesuada feugiat. Cras turpis felis, aliquet id mauris elementum, feugiat ultrices nisl.</p>
    </section>

    <p class="sign-off">Best regards,</p>
    <div class="signature" role="img" aria-label="Handwritten signature of the sender"></div>

    <div class="brand brand--footer">
      <span class="brand-dot"></span>
      <span class="brand-name">Coin Harbour Co</span>
    </div>

    <div class="footer-rule"></div>
    <footer class="contact-details">
      Address: Suite 4B Level 17, Marlowe Crest House, 9 Tindall Lane, Sydney NSW 2000 | Phone (Landline): 02 5193 4620 | Phone: 1300 4719 55 | Email: enquiries@coinharbourco.com.au | Web: www.coinharbourco.com.au<br>
      ABN: 47 381 950 623 | ASIC: 31 749218605
    </footer>
  </main>
</body>
</html>
```